Postcard and Door Hanger Design

We need two pieces designed for marketing. Both will use the same logo and photo just the text will be slightly different. We need these designs looking very modern, clean, and simple while having the important information to stand out.

Postcard: 2 sided
- Side 1 just have large logo with our website and phone number
- Side 2 below.
- 4 x 6
- Use photo of house provided
- "Going Above and Beyond Every Time"
- "Call TODAY to Reserve your project by May 1st and receive 10% off"
- "Residential and Commercial"
- Our contact is 778-294-1175
- Website is www.velmarcoatings.com
- Might include something like "check out our portfolio on our website"

Use the above as a guidline and be creative with it, add or take away as you see fit as we are open to suggestions.

Door Hanger: 2 sided
Side 1 - Logo with contact details
Side 2 - Below
- 4 x 11
- "We are painting your neighborhood"
-"come see us in action at (then leave a space where we can stick a label onto our door hanger with an address of a home we are painting)
- Call today for a FREE ESTIMATE
- 778-294-1175
- www.velmarcoatings.com

Links:

https://www.filenook.net/sh/q3k8tz52rwa9pn/TR7XKLP-QZ

https://www.filenook.net/sh/xv6rr27jtl3wyd/HNwLRaPqTs

Logo File:

https://www.filenook.net/sh/p2d94hzb1wkq07/zfa-R9LKiv

```html
<!DOCTYPE html>
<html lang="en">
<head>
<meta charset="utf-8">
<title>Velmar Coatings — Postcard Front</title>
<link rel="stylesheet" href="https://fonts.googleapis.com/css2?family=Marcellus&family=Libre+Baskerville:wght@700&display=swap">
<style>
  :root {
    --slate: #46525f;
    --teal: #00aeae;
    --white: #ffffff;
  }
  * { margin: 0; padding: 0; box-sizing: border-box; }
  html, body {
    width: 1200px;
    height: 800px;
    overflow: hidden;
    background: var(--slate);
  }
  .postcard {
    position: relative;
    width: 1200px;
    height: 800px;
    background: var(--slate);
  }
  .brand-mark {
    position: absolute;
    left: 528px;
    top: 186px;
    width: 144px;
    height: 144px;
    border-radius: 10px;
    background: var(--teal);
  }
  .brand {
    position: absolute;
    left: 0;
    right: 0;
    top: 420px;
    text-align: center;
    color: var(--white);
    font-family: "Marcellus", "Optima", serif;
    font-weight: 400;
  }
  .brand-name {
    display: block;
    font-size: 106px;
    line-height: 1;
    letter-spacing: 0.1em;
    padding-left: 0.1em;
  }
  .brand-trade {
    display: block;
    margin-top: 18px;
    font-size: 46px;
    line-height: 1;
    letter-spacing: 0.78em;
    padding-left: 0.78em;
  }
  .contact-band {
    position: absolute;
    left: 0;
    top: 661px;
    width: 1200px;
    height: 74px;
    background: var(--teal);
    display: flex;
    align-items: center;
    justify-content: center;
    gap: 36px;
    font-family: "Libre Baskerville", Georgia, serif;
    font-weight: 700;
    font-size: 40px;
    letter-spacing: 0.02em;
    color: var(--slate);
  }
  .contact-item {
    display: flex;
    align-items: center;
    gap: 12px;
  }
  .contact-icon {
    width: 38px;
    height: 38px;
    flex: none;
  }
</style>
</head>
<body>
  <main class="postcard">
    <div class="brand-mark" aria-hidden="true"></div>

    <h1 class="brand">
      <span class="brand-name">VELMAR</span>
      <span class="brand-trade">COATINGS</span>
    </h1>

    <footer class="contact-band">
      <div class="contact-item">
        <svg class="contact-icon" viewBox="0 0 24 24" aria-hidden="true">
          <path fill="#ffffff" d="M6.6 2.2c.6-.4 1.4-.2 1.8.4l2 3.2c.4.6.2 1.4-.3 1.8l-1.4 1c-.3.2-.4.6-.2 1 .9 2 2.3 3.6 4 4.9.3.2.7.2 1-.1l1.1-1.3c.5-.5 1.2-.6 1.8-.2l3.1 2.1c.6.4.8 1.2.4 1.8l-1.3 2c-.6.9-1.7 1.4-2.8 1.1C10.5 18.5 5.4 13.2 4 7.5c-.3-1.1.1-2.2 1-2.9z"/>
        </svg>
        <span class="contact-phone">778-294-1175</span>
      </div>
      <div class="contact-item">
        <svg class="contact-icon" viewBox="0 0 24 24" aria-hidden="true">
          <circle cx="12" cy="12" r="11" fill="#ffffff"/>
          <g fill="none" stroke="#00aeae" stroke-width="1.4">
            <circle cx="12" cy="12" r="8"/>
            <ellipse cx="12" cy="12" rx="3.6" ry="8"/>
            <line x1="12" y1="4" x2="12" y2="20"/>
            <line x1="4" y1="12" x2="20" y2="12"/>
            <path d="M5.5 8h13M5.5 16h13"/>
          </g>
        </svg>
        <span class="contact-web">www.velmarcoatings.com</span>
      </div>
    </footer>
  </main>
</body>
</html>
```